Asia Hotel need a card and logo

The new hotel in East Asia, Taiwan need a business card and logo design.The hotel's Chinese name is 岚溪文旅,English name is "Virel Hotel".The core concept of this hotel is "Eco green", going to use many plant etc.,The building's first outlook draft is attached in the file for your reference.The style be modern and fashion will be good. Thank you.
Target Market(s)
East Asia
Industry/Entity Type
Hotel
Contact Information for Business Card
The hotel's name both in Chinese and English :岚溪商旅 Virel Hotel
The logo, address, E-mail and tel number place.
Stuff's name and title.
Font styles to use
Colors
Designer to choose colors to be used in the design.
Look and feel
Each slider illustrates characteristics of the customer's brand and the style your logo design should communicate.

```html
<!DOCTYPE html>
<html lang="zh-Hant">
<head>
<meta charset="UTF-8">
<title>岚溪商旅 Virel Hotel — 名片</title>
<link rel="stylesheet" href="https://fonts.googleapis.com/css2?family=Jost:wght@400;500&family=Noto+Sans+TC:wght@400;500;700&display=swap">
<style>
  :root {
    --backdrop: #d4d3d4;
    --card-green: #afcda7;
    --card-green-deep: #a7c89f;
    --ink-light: #ffffff;
    --ink-soft: rgba(255, 255, 255, 0.92);
  }
  * { margin: 0; padding: 0; box-sizing: border-box; }
  html, body {
    width: 1200px;
    height: 1200px;
    overflow: hidden;
    background: var(--backdrop);
  }
  .business-card {
    position: absolute;
    left: 100px;
    top: 320px;
    width: 1000px;
    height: 560px;
    background: linear-gradient(160deg, var(--card-green-deep) 0%, var(--card-green) 55%, var(--card-green-deep) 100%);
    overflow: hidden;
    color: var(--ink-light);
    font-family: "Noto Sans TC", sans-serif;
  }
  .brand-corner {
    position: absolute;
    right: 44px;
    top: 40px;
    display: flex;
    align-items: center;
    gap: 14px;
  }
  .brand-dot {
    width: 22px;
    height: 22px;
    border-radius: 50%;
    background: var(--ink-light);
  }
  .brand-name {
    font-family: "Noto Sans TC", sans-serif;
    font-weight: 500;
    font-size: 26px;
    letter-spacing: 0.08em;
    color: var(--ink-light);
  }
  .staff-name {
    position: absolute;
    left: 50px;
    top: 112px;
    font-size: 32px;
    font-weight: 700;
    letter-spacing: 0.28em;
  }
  .staff-title {
    position: absolute;
    left: 50px;
    top: 160px;
    font-size: 20px;
    font-weight: 400;
    letter-spacing: 0.3em;
  }
  .contact-list {
    position: absolute;
    left: 50px;
    top: 228px;
    list-style: none;
  }
  .contact-list li {
    color: var(--ink-soft);
    white-space: nowrap;
  }
  .contact-address {
    font-size: 22px;
    letter-spacing: 0.02em;
    margin-bottom: 10px;
  }
  .contact-address .label,
  .contact-line .label {
    font-family: "Jost", sans-serif;
    font-size: 16px;
  }
  .contact-line {
    font-family: "Jost", sans-serif;
    font-size: 17px;
    letter-spacing: 0.1em;
    line-height: 28px;
  }
  .contact-tax {
    font-size: 20px;
    line-height: 28px;
  }
  .contact-tax .value {
    font-family: "Jost", sans-serif;
    font-size: 16px;
    letter-spacing: 0.1em;
  }
  .company-block {
    position: absolute;
    left: 50px;
    top: 396px;
  }
  .company-web {
    font-family: "Jost", sans-serif;
    font-size: 16px;
    letter-spacing: 0.12em;
    color: var(--ink-soft);
  }
  .company-name {
    margin-top: 6px;
    font-size: 22px;
    letter-spacing: 0.04em;
    color: var(--ink-soft);
  }
</style>
</head>
<body>
  <section class="business-card" aria-label="岚溪商旅 Virel Hotel 名片">
    <div class="brand-corner">
      <span class="brand-name">Virel Hotel</span>
      <span class="brand-dot" aria-hidden="true"></span>
    </div>

    <h1 class="staff-name">林柏宇</h1>
    <p class="staff-title">經理</p>

    <ul class="contact-list">
      <li class="contact-address"><span class="label">A:</span>台中市南屯區文心路二段88巷12號</li>
      <li class="contact-line"><span class="label">E:</span> hi@virelhotel.com</li>
      <li class="contact-line"><span class="label">P:</span> 0912-345-678</li>
      <li class="contact-tax">統編：<span class="value">53917284</span></li>
    </ul>

    <div class="company-block">
      <p class="company-web">www.virelhotel.com</p>
      <p class="company-name">岚溪開發股份有限公司</p>
    </div>
  </section>
</body>
</html>
```